Business Card Design

I would like a new business card design for an accounting firm that specializes in resolving clients tax problems. I want the card to give the impression that we are not your typical stodgy accounting firm, but at the same time we will get the job done.
Industry/Entity Type
Business
Contact Information for Business Card
Dorian T Welsby
Certified Public Accountant
38-27 52nd Street
Sunnyside, NY 11287
Tel: (718) 555-0142
Fax: (888) 555-0199
e-mail: dtwthecpa@ledgerpost.com
website: harborfilingreliefexperts.com

```html
<!DOCTYPE html>
<html lang="en">
<head>
<meta charset="utf-8">
<title>Dorian T Welsby – Business Card</title>
<link rel="stylesheet" href="https://fonts.googleapis.com/css2?family=Share+Tech+Mono&family=Open+Sans:wght@400&display=swap">
<style>
  :root {
    --card-dark: #231f20;
    --brand-gold: #b9a466;
    --ink-white: #ffffff;
    --page-bg: #ffffff;
  }
  * { margin: 0; padding: 0; box-sizing: border-box; }
  html, body {
    width: 1200px; height: 727px; overflow: hidden;
    background: var(--page-bg);
  }
  .business-card {
    position: relative;
    width: 1200px; height: 727px;
    background: var(--card-dark);
    border-radius: 50px;
    overflow: hidden;
    font-family: "Open Sans", "Segoe UI", sans-serif;
    color: var(--ink-white);
  }
  .name-plate {
    position: absolute; left: 0; top: 0;
    width: 607px; height: 155px;
    background: var(--brand-gold);
    font-family: "Share Tech Mono", monospace;
  }
  .person-name {
    position: absolute; left: 40px; top: 30px;
    font-size: 74px; line-height: 1; letter-spacing: 2px;
    font-weight: 400; white-space: nowrap;
  }
  .person-title {
    position: absolute; left: 66px; top: 105px;
    font-size: 34px; line-height: 1; letter-spacing: 1px;
    white-space: nowrap;
  }
  .contact-row { position: absolute; left: 0; width: 100%; }
  .row-bar {
    position: absolute; left: 0;
    width: 150px; height: 70px;
    background: var(--brand-gold);
  }
  .row-badge {
    position: absolute; left: 100px;
    width: 104px; height: 104px;
  }
  .row-text {
    position: absolute; left: 238px;
    font-size: 42px; line-height: 56px;
    white-space: nowrap;
  }
  .row-address { top: 220px; }
  .row-address .row-bar { top: 21px; }
  .row-address .row-badge { top: 4px; }
  .row-address .row-text { top: 0; }
  .row-phone { top: 353px; }
  .row-phone .row-bar { top: 17px; }
  .row-phone .row-badge { top: 0; }
  .row-phone .row-text { top: 22px; }
  .row-fax { top: 477px; }
  .row-fax .row-bar { top: 17px; }
  .row-fax .row-badge { top: 0; }
  .row-fax .row-text { top: 24px; }
  .footer-band {
    position: absolute; left: 0; bottom: 0;
    width: 100%; height: 103px;
    background: var(--brand-gold);
    font-size: 33px;
  }
  .footer-item {
    position: absolute; top: 0; height: 103px;
    display: flex; align-items: center; gap: 14px;
    white-space: nowrap;
  }
  .footer-email { left: 31px; }
  .footer-web { left: 565px; }
</style>
</head>
<body>
<div class="business-card">
  <header class="name-plate">
    <h1 class="person-name">Dorian T Welsby</h1>
    <p class="person-title">Certified Public Accountant</p>
  </header>

  <section class="contact-row row-address">
    <div class="row-bar"></div>
    <svg class="row-badge" viewBox="0 0 104 104" aria-hidden="true">
      <circle cx="52" cy="52" r="52" fill="var(--brand-gold)"/>
      <circle cx="52" cy="52" r="37" fill="var(--card-dark)"/>
      <path d="M52 30 L76 52 L70 52 L70 72 L58 72 L58 60 L46 60 L46 72 L34 72 L34 52 L28 52 Z" fill="var(--ink-white)"/>
      <rect x="63" y="34" width="5" height="10" fill="var(--ink-white)"/>
    </svg>
    <p class="row-text">38-27 52nd Street<br>Sunnyside, NY 11287</p>
  </section>

  <section class="contact-row row-phone">
    <div class="row-bar"></div>
    <svg class="row-badge" viewBox="0 0 104 104" aria-hidden="true">
      <circle cx="52" cy="52" r="52" fill="var(--brand-gold)"/>
      <circle cx="52" cy="52" r="37" fill="var(--card-dark)"/>
      <path d="M28 44 Q28 34 52 34 Q76 34 76 44 L76 48 L65 48 L65 42 L39 42 L39 48 L28 48 Z" fill="var(--ink-white)"/>
      <path d="M38 52 L66 52 L72 74 L32 74 Z" fill="var(--ink-white)"/>
      <circle cx="52" cy="62" r="7" fill="var(--card-dark)"/>
      <circle cx="52" cy="62" r="3" fill="var(--ink-white)"/>
    </svg>
    <p class="row-text">(718) 555-0142</p>
  </section>

  <section class="contact-row row-fax">
    <div class="row-bar"></div>
    <svg class="row-badge" viewBox="0 0 104 104" aria-hidden="true">
      <circle cx="52" cy="52" r="52" fill="var(--brand-gold)"/>
      <circle cx="52" cy="52" r="37" fill="var(--card-dark)"/>
      <rect x="43" y="27" width="24" height="22" fill="var(--ink-white)"/>
      <rect x="47" y="32" width="16" height="2" fill="var(--card-dark)"/>
      <rect x="47" y="37" width="16" height="2" fill="var(--card-dark)"/>
      <rect x="47" y="42" width="16" height="2" fill="var(--card-dark)"/>
      <rect x="31" y="44" width="8" height="30" rx="3" fill="var(--ink-white)"/>
      <rect x="41" y="51" width="35" height="23" rx="2" fill="var(--ink-white)"/>
      <rect x="46" y="56" width="25" height="4" fill="var(--card-dark)"/>
    </svg>
    <p class="row-text">(888) 555-0199</p>
  </section>

  <footer class="footer-band">
    <div class="footer-item footer-email">
      <svg width="56" height="40" viewBox="0 0 56 40" aria-hidden="true">
        <rect x="1.5" y="1.5" width="53" height="37" fill="var(--ink-white)" stroke="var(--ink-white)"/>
        <path d="M2 2 L28 24 L54 2 M2 38 L21 18 M54 38 L35 18" fill="none" stroke="var(--brand-gold)" stroke-width="2"/>
      </svg>
      <span>:&nbsp;dtwthecpa@ledgerpost.com</span>
    </div>
    <div class="footer-item footer-web">
      <svg width="50" height="50" viewBox="0 0 50 50" aria-hidden="true">
        <g fill="none" stroke="var(--ink-white)" stroke-width="3">
          <circle cx="25" cy="25" r="22"/>
          <ellipse cx="25" cy="25" rx="10" ry="22"/>
          <line x1="25" y1="3" x2="25" y2="47"/>
          <line x1="3" y1="25" x2="47" y2="25"/>
          <path d="M7 13 H43 M7 37 H43"/>
        </g>
      </svg>
      <span>:&nbsp;harborfilingreliefexperts.com</span>
    </div>
  </footer>
</div>
</body>
</html>
```